Mental Health

KVR HAVEN
Behavioral Health
4172 E. Dorrel St. Mesa, AZ 85217
Marguerite (480)555-0142 / Ivan 480-555-0187

Email: KVRHaven@Qortamail.com
Newly Remodeled & Spacious
g Staff
Registered Nurses
Licensed Independent &
Professional Substance &
Abuse Counselors
Behavioral Health Techs
Certified Caregivers
Behavioral Health &
Substance Abuse Professionals

To Refer a Patient
About Us
KVR Haven is a Fully Staffed Behavioral
Health Residential Facility, providing
treatment plans for adults suffering
with various Behavioral Health and
Substance Abuse disorders, while living
in a nice safe, clean and supportive
environment. Our home offers clients the
ability to learn the necessary skills to
help clients adapt, build self confidence
as well as independence, with the goal
of reducing the probability of a future
crisis or possible relapse. We offer
counseling programs, consisting of a
variety of addiction and recovery support
groups, independent living, coping and
social skills groups, as well as assisting
clients with using tools to create a resume
to help obtain employment and so much
more. We are committed to teaching
self management care and allowing
clients to understand how to utilize the
resources, skills and tools available for
long term success by providing superior
quality, all-inclusive living arrangements
and treatment options.

Thank you for your patience while I update the final content needed for us to make the final decision this week.

```html
<!DOCTYPE html>
<html lang="en">
<head>
<meta charset="utf-8">
<title>KVR Haven — Business Cards</title>
<link rel="stylesheet" href="https://fonts.googleapis.com/css2?family=Arimo:wght@400;700&family=Oswald:wght@500&display=swap">
<style>
  :root {
    --stage: #0e0e0e;
    --card: #171717;
    --blue: #1673c4;
    --green: #7db533;
    --orange: #ef6a24;
    --white: #f2f2f2;
  }
  * { box-sizing: border-box; margin: 0; padding: 0; }
  html, body { width: 1200px; height: 900px; overflow: hidden; background: var(--stage); }
  .stage { position: relative; width: 1200px; height: 900px; }
  .card {
    position: absolute; left: 320px; width: 560px; height: 320px;
    background: var(--card); overflow: hidden;
    font-family: "Arimo", Arial, sans-serif;
    box-shadow: 0 10px 30px rgba(0,0,0,.6);
  }
  .card--front { top: 95px; }
  .card--back { top: 480px; }
  .card__band {
    position: absolute; left: 0; right: 0; bottom: 0; height: 9px;
    background: linear-gradient(to right, var(--blue) 0 55%, var(--green) 55% 100%);
  }
  /* front */
  .brand {
    position: absolute; top: 62px; left: 0; right: 0;
    display: flex; align-items: center; justify-content: center; gap: 16px;
  }
  .brand__dot { width: 58px; height: 58px; border-radius: 50%; background: var(--green); }
  .brand__name { font-size: 46px; font-weight: 400; color: var(--blue); letter-spacing: 1px; }
  .services {
    position: absolute; top: 170px; left: 20px; right: 20px;
    text-align: center; color: var(--green); font-size: 14.5px; line-height: 1.45;
  }
  .services .sep { color: var(--blue); padding: 0 4px; }
  /* back */
  .contacts {
    position: absolute; top: 48px; left: 0; right: 0;
    display: flex; justify-content: center; align-items: stretch; gap: 28px;
  }
  .contact { display: flex; flex-direction: column; }
  .contact--left { align-items: flex-end; }
  .contact--right { align-items: flex-start; padding-top: 26px; }
  .contact__name {
    font-family: "Oswald", "Arial Narrow", sans-serif; font-weight: 500;
    font-size: 36px; line-height: 1; color: var(--blue); text-transform: uppercase;
  }
  .contact__phone {
    display: flex; align-items: center; gap: 6px; margin-top: 6px;
    color: var(--white); font-size: 17px;
  }
  .contact__phone svg { width: 16px; height: 16px; }
  .contacts__divider { width: 1.5px; background: var(--blue); margin-top: 18px; height: 68px; }
  .email {
    position: absolute; top: 168px; left: 0; right: 0; text-align: center;
    color: var(--orange); font-size: 18px;
  }
  .company {
    position: absolute; top: 218px; left: 0; right: 0; text-align: center;
    color: var(--blue); font-size: 19px; font-weight: 700;
  }
  .address {
    position: absolute; top: 246px; left: 0; right: 0; text-align: center;
    color: var(--white); font-size: 16px;
  }
</style>
</head>
<body>
<main class="stage">
  <section class="card card--front">
    <div class="brand">
      <span class="brand__dot"></span>
      <span class="brand__name">KVR Haven</span>
    </div>
    <p class="services">
      Newly Remodeled &amp; Spacious<span class="sep">|</span>General Staff<span class="sep">|</span>Registered Nurses<br>
      Licensed Independent<span class="sep">|</span>Professional Substance<span class="sep">|</span>Abuse Counselors<br>
      Behavioral Health Techs<span class="sep">|</span>Certified Caregivers<span class="sep">|</span>Behavioral Health<br>
      Substance Abuse Professionals
    </p>
    <div class="card__band"></div>
  </section>

  <section class="card card--back">
    <div class="contacts">
      <div class="contact contact--left">
        <h2 class="contact__name">Marguerite</h2>
        <p class="contact__phone">(480)555-0142
          <svg viewBox="0 0 24 24" aria-hidden="true"><path fill="var(--green)" d="M6.6 10.8a15.1 15.1 0 0 0 6.6 6.6l2.2-2.2c.3-.3.7-.4 1-.2 1.1.4 2.3.6 3.6.6.6 0 1 .4 1 1V20c0 .6-.4 1-1 1A17 17 0 0 1 3 4c0-.6.4-1 1-1h3.5c.6 0 1 .4 1 1 0 1.3.2 2.5.6 3.6.1.3 0 .7-.2 1z"/></svg>
        </p>
      </div>
      <span class="contacts__divider"></span>
      <div class="contact contact--right">
        <h2 class="contact__name">Ivan</h2>
        <p class="contact__phone">
          <svg viewBox="0 0 24 24" aria-hidden="true"><path fill="var(--green)" d="M6.6 10.8a15.1 15.1 0 0 0 6.6 6.6l2.2-2.2c.3-.3.7-.4 1-.2 1.1.4 2.3.6 3.6.6.6 0 1 .4 1 1V20c0 .6-.4 1-1 1A17 17 0 0 1 3 4c0-.6.4-1 1-1h3.5c.6 0 1 .4 1 1 0 1.3.2 2.5.6 3.6.1.3 0 .7-.2 1z"/></svg>
          480-555-0187</p>
      </div>
    </div>
    <p class="email">KVRHaven@Qortamail.com</p>
    <p class="company">KVR HAVEN</p>
    <p class="address">Behavioral Health, 4172 E. Dorrel St. Mesa, AZ 85217</p>
    <div class="card__band"></div>
  </section>
</main>
</body>
</html>
```